Marwood Holiday Jubilee 2025

We’re looking for a designer to help refresh the visual identity of our annual Christmas show while maintaining continuity from previous years. The updated design should feel festive, and warm, with a sense of celebration and anticipation. We’d like a central graphic that can be adapted for posters, social media, and digital signage, along with supporting assets for flyers and banners.

We’re open to seasonal color palettes such as rich reds, deep greens or blues, golds, silvers, or cool winter tones, and prefer typography that’s clear and elegant. The overall look should feel familiar to returning audiences while inviting and engaging for newcomers.

Two key groups: the current attenders of our congregation and the broader community in our suburb of Rochester, NY. Our congregation is made up of families, older adults, and young professionals who value faith, community and spiritual growth. The surrounding community is a fast growing friendly and family-oriented area of young professionals and longtime families.

We’re looking for a designer to help refresh the visual identity of our annual Christmas show while maintaining continuity with the theme and tone of previous years. The updated design should feel festive, and warm, with a sense of celebration and anticipation. We’d like a central graphic that can be adapted for posters, social media, and digital signage, along with supporting assets for flyers and banners.

Target Market(s)

Two key groups: the current attenders of our congregation and the broader community in our suburb of Rochester, NY. Our congregation is made up of families, older adults, and young professionals who value faith, community and spiritual growth. The surrounding community is a fast growing friendly and family-oriented area of young professionals and long time families.

Industry/Entity Type

Non-profit. Church

Font styles to use
Serif
Decorative
Script
Other font styles liked:
• Quentin

Requirements
Must have
• Sparkle, eye catching
Should not have
• must not look identical to the uploaded versions

```html
<!DOCTYPE html>
<html lang="en">
<head>
<meta charset="utf-8">
<title>Marwood Holiday Jubilee</title>
<link href="https://fonts.googleapis.com/css2?family=Cinzel:wght@600&family=Bebas+Neue&family=Great+Vibes&family=Montserrat:wght@600&display=swap" rel="stylesheet">
<style>
  :root {
    --night: #050b18;
    --night-deep: #02050d;
    --aurora: #1f9a78;
    --aurora-bright: #2fe06e;
    --mint: #4ff0c8;
    --mint-soft: #9ff8e2;
    --frost: #ffffff;
  }
  html, body {
    margin: 0;
    padding: 0;
    width: 1200px;
    height: 711px;
    overflow: hidden;
    background: var(--night);
  }
  .poster {
    position: relative;
    width: 1200px;
    height: 711px;
    overflow: hidden;
  }
  .winter-sky {
    position: absolute;
    inset: 0;
    background:
      radial-gradient(ellipse 560px 70px at 250px 105px, rgba(31, 154, 120, 0.7), transparent 70%),
      radial-gradient(ellipse 520px 90px at 980px 150px, rgba(31, 154, 120, 0.6), transparent 70%),
      radial-gradient(ellipse 200px 160px at 290px 260px, rgba(60, 200, 170, 0.45), transparent 70%),
      radial-gradient(ellipse 220px 70px at 720px 205px, rgba(31, 154, 120, 0.5), transparent 70%),
      radial-gradient(ellipse 260px 55px at 960px 400px, rgba(47, 224, 110, 0.75), transparent 70%),
      radial-gradient(ellipse 420px 120px at 860px 330px, rgba(31, 154, 120, 0.35), transparent 70%),
      linear-gradient(180deg, #04101a 0%, #0a1c2c 42%, #0d1a36 60%, #0a1228 75%, var(--night-deep) 100%);
  }
  .event-art {
    position: absolute;
    inset: 0;
  }
  .host {
    font-family: "Cinzel", serif;
    font-weight: 600;
    fill: var(--frost);
    letter-spacing: 1.5px;
  }
  .title {
    font-family: "Bebas Neue", sans-serif;
    fill: url(#frost-fill);
  }
  .script {
    font-family: "Great Vibes", cursive;
    fill: url(#frost-fill);
  }
  .date {
    font-family: "Montserrat", sans-serif;
    font-weight: 600;
    fill: var(--mint);
    letter-spacing: 5px;
  }
  .time {
    font-family: "Montserrat", sans-serif;
    font-weight: 600;
    fill: var(--frost);
    letter-spacing: 5px;
  }
</style>
</head>
<body>
  <main class="poster">
    <div class="winter-sky" role="img" aria-label="Starry night sky with green northern lights over a snowy pine forest and a lit cabin, with falling snow"></div>
    <svg class="event-art" width="1200" height="711" viewBox="0 0 1200 711" xmlns="http://www.w3.org/2000/svg">
      <defs>
        <linearGradient id="frost-fill" gradientUnits="userSpaceOnUse" x1="190" y1="0" x2="1030" y2="0">
          <stop offset="0" stop-color="var(--mint)"/>
          <stop offset="0.45" stop-color="var(--mint-soft)"/>
          <stop offset="0.75" stop-color="var(--frost)"/>
          <stop offset="1" stop-color="var(--mint-soft)"/>
        </linearGradient>
        <filter id="glitter" x="-5%" y="-10%" width="115%" height="130%">
          <feTurbulence type="fractalNoise" baseFrequency="0.11" numOctaves="2" seed="4" result="noiseA"/>
          <feColorMatrix in="noiseA" type="matrix" values="0 0 0 0 0.25  0 0 0 0 0.9  0 0 0 0 0.75  14 0 0 0 -7.2" result="mintSpots"/>
          <feComposite in="mintSpots" in2="SourceAlpha" operator="in" result="mintIn"/>
          <feTurbulence type="fractalNoise" baseFrequency="0.16" numOctaves="2" seed="11" result="noiseB"/>
          <feColorMatrix in="noiseB" type="matrix" values="0 0 0 0 1  0 0 0 0 1  0 0 0 0 1  0 16 0 0 -9" result="whiteSpots"/>
          <feComposite in="whiteSpots" in2="SourceAlpha" operator="in" result="whiteIn"/>
          <feGaussianBlur in="SourceAlpha" stdDeviation="3" result="blur"/>
          <feOffset in="blur" dx="4" dy="5" result="offset"/>
          <feFlood flood-color="#000" flood-opacity="0.75"/>
          <feComposite in2="offset" operator="in" result="shadow"/>
          <feMerge>
            <feMergeNode in="shadow"/>
            <feMergeNode in="SourceGraphic"/>
            <feMergeNode in="mintIn"/>
            <feMergeNode in="whiteIn"/>
          </feMerge>
        </filter>
        <filter id="lift" x="-10%" y="-20%" width="120%" height="150%">
          <feDropShadow dx="3" dy="4" stdDeviation="3" flood-color="#000" flood-opacity="0.75"/>
        </filter>
      </defs>
      <text class="host" x="608" y="117" text-anchor="middle" font-size="33">CEDAR LANE BAPTIST CHURCH</text>
      <text class="host" x="608" y="146" text-anchor="middle" font-size="23">PRESENT</text>
      <text class="title" x="194" y="364" font-size="200" textLength="829" lengthAdjust="spacingAndGlyphs" filter="url(#glitter)">MARWOOD HOLIDAY</text>
      <text class="script" x="612" y="458" text-anchor="middle" font-size="170" filter="url(#glitter)">Jubilee</text>
      <text class="date" x="609" y="563" text-anchor="middle" font-size="42" filter="url(#glitter)">DECEMBER 16 &amp; 17</text>
      <text class="time" x="592" y="615" text-anchor="middle" font-size="42" filter="url(#lift)">6 : 00 PM</text>
    </svg>
  </main>
</body>
</html>
```